Bref créative
Summit Fairway Swing Institute
Redefining Golf Instruction
Professional
Brian Lockwell
Founder
(no physical address to be printed on business card or stationary)
brian@sfsinstitute.net
www.sfsinstitute.net
(Please include the RMX, DORAL and PLUF logos somewhere on the card)
* Full Round Review (FRR)
* On Course Coaching Sessions
* Junior Tournament Prep
* PLUF Beginner Classes
* Corporate Events
* Birthday Parties
Main company logo
Affiliation logo
Affiliation logo (on back of card)

```html
<!DOCTYPE html>
<html lang="en">
<head>
<meta charset="utf-8">
<title>Summit Fairway Swing Institute – Stationery Set</title>
<link href="https://fonts.googleapis.com/css2?family=Cinzel:wght@600&family=Open+Sans:wght@400;600;700&display=swap" rel="stylesheet">
<style>
:root{
  --stage:#1c1c1e;
  --stage-light:#2b2b2e;
  --red:#c8102e;
  --ink:#222;
  --grey:#777;
  --paper:#ffffff;
  --black-card:#111;
  --label:#8d8d8d;
  --badge-light:#d9d9d9;
  --badge-dark:#444;
}
*{box-sizing:border-box;margin:0;padding:0}
html,body{width:1200px;height:410px;overflow:hidden}
body{background:var(--stage);font-family:"Open Sans",Arial,sans-serif;position:relative}
.board{position:absolute;inset:0;background:linear-gradient(180deg,var(--stage-light),var(--stage))}
.abs{position:absolute}
.brand-name{font-family:"Cinzel",Georgia,serif;font-weight:600;letter-spacing:.03em;text-transform:uppercase;line-height:1.15}
.mark{border-radius:50%;background:var(--red);display:inline-block}
.caption{position:absolute;font-size:7px;color:var(--label);text-align:center;white-space:nowrap}

/* hero logo */
.hero{left:60px;top:8px;width:204px;text-align:center}
.hero .mark{width:56px;height:56px}
.hero .brand-name{color:#fff;font-size:15px;margin-top:4px}
.hero .tag{color:#aaa;font-size:8px;margin-top:14px}

/* cards */
.card{position:absolute;width:150px;height:84px;background:var(--paper);overflow:hidden;box-shadow:0 2px 6px rgba(0,0,0,.5)}
.card.dark{background:var(--black-card)}
.card .strip{position:absolute;left:0;right:0;bottom:0;height:7px;background:var(--red)}
.card .brand-name{font-size:5.5px;color:var(--ink)}
.card.dark .brand-name{color:#fff}
.card .mark{width:20px;height:20px}
.card .mini{font-size:5px;color:var(--grey);line-height:1.5;white-space:nowrap}
.card .mini b{color:var(--ink)}
.list{font-size:5px;line-height:1.6;color:var(--ink);white-space:nowrap}
.card.dark .list{color:#eee}
.badge{width:24px;height:9px;border-radius:2px;background:var(--badge-light)}
.card.dark .badge{background:var(--badge-dark)}
.badges{display:flex;gap:4px}

/* letterhead */
.letterhead{left:530px;top:22px;width:272px;height:372px;background:var(--paper);box-shadow:0 3px 8px rgba(0,0,0,.5);overflow:hidden}
.letterhead .head{position:absolute;left:16px;top:18px;width:78px;text-align:center}
.letterhead .mark{width:22px;height:22px}
.letterhead .brand-name{font-size:5.5px;color:var(--ink);margin-top:2px}
.letterhead .contact{position:absolute;left:150px;top:20px;font-size:4.5px;color:var(--grey);line-height:1.6;white-space:nowrap}
.letterhead .ghost{position:absolute;left:78px;top:135px;width:120px;height:140px;border-radius:50%;background:var(--red);opacity:.07}
.letterhead .foot{position:absolute;left:0;right:0;bottom:0;height:4px;background:var(--red)}

/* envelopes */
.env{position:absolute;box-shadow:0 3px 8px rgba(0,0,0,.5);overflow:hidden}
.env .flap{position:absolute;left:0;top:0;width:100%;height:100%}
.env.back{left:840px;top:72px;width:354px;height:115px;background:var(--black-card)}
.env.plain{left:930px;top:80px;width:264px;height:100px;background:#f2f2f2}
.env.front{left:818px;top:176px;width:376px;height:210px;background:var(--paper)}
.env .ret{position:absolute;left:22px;top:92px;width:70px;text-align:center}
.env .ret .mark{width:20px;height:20px}
.env .ret .brand-name{font-size:5px;color:var(--ink);margin-top:2px}
.env .ret .mini{font-size:4.3px;color:var(--grey);margin-top:2px}
.env .ghost{position:absolute;left:150px;top:70px;width:100px;height:120px;border-radius:50%;background:var(--red);opacity:.07}
.env .foot{position:absolute;left:0;right:0;bottom:0;height:4px;background:var(--red)}
</style>
</head>
<body>
<div class="board"></div>

<div class="abs hero">
  <span class="mark"></span>
  <div class="brand-name">Summit Fairway<br>Swing Institute</div>
  <div class="tag">Redefining Golf Instruction</div>
</div>

<!-- business card fronts -->
<div class="card" style="left:108px;top:156px">
  <div class="abs" style="left:8px;top:12px;width:60px;text-align:center">
    <span class="mark"></span>
    <div class="brand-name" style="margin-top:2px">Summit Fairway Swing Institute</div>
  </div>
  <div class="abs mini" style="left:78px;top:12px">
    <b>Brian Lockwell</b><br>Founder<br>(555) 014-2290<br>brian@sfsinstitute.net<br>www.sfsinstitute.net
  </div>
  <div class="strip"></div>
</div>
<div class="caption" style="left:108px;top:246px;width:150px">Business Card Front A</div>

<div class="card" style="left:268px;top:156px">
  <div class="abs" style="left:8px;top:12px;width:60px;text-align:center">
    <span class="mark"></span>
    <div class="brand-name" style="margin-top:2px">Summit Fairway Swing Institute</div>
  </div>
  <div class="abs mini" style="left:78px;top:12px">
    <b>Brian Lockwell</b><br>Founder<br>(555) 014-2290<br>brian@sfsinstitute.net<br>www.sfsinstitute.net
  </div>
  <div class="strip"></div>
</div>
<div class="caption" style="left:268px;top:246px;width:150px">Business Card Front B</div>

<!-- card backs -->
<div class="card" style="left:22px;top:276px">
  <div class="abs" style="left:8px;top:9px;display:flex;flex-direction:column;gap:5px">
    <div class="badge"></div><div class="badge"></div><div class="badge"></div>
  </div>
  <div class="abs list" style="left:42px;top:8px">
    • Full Round Review<br>• On Course Coaching<br>• Junior Tournament Prep<br>• Beginner Group Classes<br>• Corporate Events<br>• Birthday Parties
  </div>
  <div class="strip"></div>
</div>
<div class="caption" style="left:22px;top:364px;width:150px">Card Back A</div>

<div class="card" style="left:186px;top:276px">
  <div class="abs" style="left:0;top:0;width:40px;height:77px;background:var(--red)"></div>
  <div class="abs" style="left:10px;top:28px"><span class="mark" style="background:#fff"></span></div>
  <div class="abs list" style="left:48px;top:8px">
    • Full Round Review<br>• On Course Coaching<br>• Junior Tournament Prep<br>• Beginner Group Classes<br>• Corporate Events<br>• Birthday Parties
  </div>
  <div class="strip"></div>
</div>
<div class="caption" style="left:186px;top:364px;width:150px">Card Back B</div>

<div class="card dark" style="left:350px;top:276px">
  <div class="abs" style="left:10px;top:12px;width:56px;text-align:center">
    <span class="mark"></span>
    <div class="brand-name" style="margin-top:2px">Summit Fairway Swing Institute</div>
  </div>
  <div class="abs badges" style="left:78px;top:54px">
    <div class="badge"></div><div class="badge"></div>
  </div>
  <div class="strip"></div>
</div>
<div class="caption" style="left:350px;top:364px;width:150px">Card Back C</div>

<div class="card dark" style="left:514px;top:276px;display:none"></div>

<!-- letterhead -->
<div class="abs letterhead">
  <div class="head">
    <span class="mark"></span>
    <div class="brand-name">Summit Fairway Swing Institute</div>
  </div>
  <div class="contact">(555) 014-2290<br>brian@sfsinstitute.net<br>www.sfsinstitute.net</div>
  <div class="ghost"></div>
  <div class="foot"></div>
</div>
<div class="caption" style="left:530px;top:398px;width:272px">Letterhead</div>

<!-- envelopes -->
<div class="env back">
  <svg class="flap" viewBox="0 0 354 115" preserveAspectRatio="none">
    <polygon points="0,0 354,0 177,70" fill="#fff"/>
  </svg>
</div>
<div class="env plain">
  <svg class="flap" viewBox="0 0 264 100" preserveAspectRatio="none">
    <polygon points="0,0 264,0 132,55" fill="#e4e4e4"/>
  </svg>
</div>
<div class="env front">
  <svg class="flap" viewBox="0 0 376 210" preserveAspectRatio="none">
    <polygon points="0,0 376,0 376,32 188,62 0,32" fill="var(--red)"/>
  </svg>
  <div class="ret">
    <span class="mark"></span>
    <div class="brand-name">Summit Fairway Swing Institute</div>
    <div class="mini">www.sfsinstitute.net</div>
  </div>
  <div class="ghost"></div>
  <div class="foot"></div>
</div>
<div class="caption" style="left:818px;top:398px;width:376px">Envelope</div>
</body>
</html>
```